Linkedin banner Photoshop template for advertising

I need 2 PHOTOSHOP templates to advertise on linkedin. I will attach examples of what I would like to have. Everything must be% 26 # 234; done with PHOTOSHOP with layers so that I can r% 26 # 233; use the template during my future publications Pub # 1 New clients J% 26 # 39; I made a sketch which is attached and here is d% 26 # 233; finishing the points num% 26 # 233; rot% 26 # 233; 1-% 26 # 201; writing: Ferlin Solutions is proud to count among its customers: 2- Framed area% 26 # 233; that I'm going to be able to place my new customers' logo. 3- Footer. Have my logo on a black background with my slogan: call center sp% 26 # 233; cialis% 26 # 233; for car dealers. 4- Put an image in the background. In this case it is an image of a car with a landscape. To do this editing. I would like to have an image of a Voltane and to have the logo of Voltane Marquet% 26 # 224; montr% 26 # 233; al, Canada Pub # 2 Advert employee% 26 # 233; I have made a sketch which is attached and here is d% 26 # 233; finishing of the points num% 26 # 233; rot% 26 # 233; 1-% 26 # 201; writing: Ferlin Solutions is proud to count among its employees% 26 # 233; s: 2- Framed area% 26 # 233; that I will% 26 # 234; be able to place the photo of my employee% 26 # 233; 3- Footer. Have my logo on a black background with my slogan: call center sp% 26 # 233; cialis% 26 # 233; for car dealers. 4- Put an image in the background. In this case I would like a call center and an employee% 26 # 233; with a helmet see attached image I want this to be professional and represent my brand. The assemblies must not be% 26 # 234; overloaded% 26 # 233 ;. I would also like the framing and editing to be a professional finish. Maybe use some short shade I let you work and impress me. I also invite you% 26 # 224; go to linkedin to see the ads that are displayed to give you an id% 26 # 233; e. I remain available for discussion at any time. If you have any questions, don't site.

Target Market(s)

R% 26 # 233; Linkedin bucket

Industry/Entity Type

Automotive

Colors

Designer to choose colors to be used in the design.

Requirements
Must have
• Everything must be% 26 # 234; done with PHOTOSHOP with layers so that I can r% 26 # 233; use the template during my future publications. Go to my website www.ferlinsolutions-exemple.ca
Nice to have
• I have made a sketch which is attached and here is d% 26 # 233; finishing of the points num% 26 # 233; rot% 26 # 233; 1-% 26 # 201; writing: Ferlin Solutions is proud to count among its customers: 2- Framed area% 26 # 233; that I'm going to be able to place my new customers' logo. 3- Footer. Have my logo on a black background with my slogan: call center sp% 26 # 233; cialis% 26 # 233; for car dealers. 4- Put an image in the background. In this case it is an image of a car with a landscape.
Should not have
• bright colors.

```html
<!DOCTYPE html>
<html lang="fr">
<head>
<meta charset="utf-8">
<title>Ferlin Solutions – bannières LinkedIn</title>
<link rel="stylesheet" href="https://fonts.googleapis.com/css2?family=Poppins:wght@300;400;600;800&display=swap">
<style>
  :root {
    --page: #ffffff;
    --ink: #0a0a0b;
    --panel: #111214;
    --blue: #1f7ad8;
    --blue-deep: #17488f;
    --white: #ffffff;
    --steel-1: #5d6066;
    --steel-2: #1d1e21;
  }
  * { margin: 0; padding: 0; box-sizing: border-box; }
  html, body { width: 1094px; height: 1200px; overflow: hidden; background: var(--page); }
  body { position: relative; font-family: "Poppins", sans-serif; color: var(--white); }

  .banner {
    position: absolute; left: 53px; width: 986px; height: 515px;
    background: var(--ink); overflow: hidden;
  }
  .banner--employee { top: 51px; }
  .banner--client { top: 619px; }

  .banner__photo { position: absolute; top: 0; right: 0; height: 420px; }
  .banner--employee .banner__photo {
    width: 620px;
    background:
      linear-gradient(90deg, var(--ink) 0%, rgba(10,10,11,0.6) 25%, rgba(10,10,11,0) 55%),
      radial-gradient(ellipse at 78% 45%, #c89a84 0%, #7a5a4c 30%, #3a3532 60%, #1b1b1d 100%);
  }
  .banner--client .banner__photo {
    width: 640px;
    background:
      linear-gradient(90deg, var(--ink) 0%, rgba(10,10,11,0.55) 28%, rgba(10,10,11,0) 55%),
      linear-gradient(180deg, #4d5a3f 0%, #8a8b83 30%, #6f7378 60%, #4f5862 100%);
  }

  .banner__shapes { position: absolute; inset: 0; width: 986px; height: 515px; }

  .headline {
    position: absolute; left: 53px; font-weight: 300; line-height: 1.33;
    letter-spacing: 0.2px;
  }
  .headline strong { color: var(--blue); font-weight: 800; }
  .banner--employee .headline { top: 70px; font-size: 33px; width: 520px; }
  .banner--client .headline { top: 85px; font-size: 35px; line-height: 1.3; }

  .employee-portrait {
    position: absolute; left: 55px; top: 180px; width: 168px; height: 168px;
    border-radius: 50%; border: 5px solid var(--blue);
    background: radial-gradient(circle at 50% 40%, #b9c2cc 0%, #6f7f94 45%, #2c3e5e 100%);
  }
  .employee-name {
    position: absolute; left: 56px; top: 364px;
    font-size: 14px; font-weight: 600; letter-spacing: 0.6px;
  }
  .employee-name::before {
    content: ""; display: inline-block; width: 13px; height: 2px;
    background: var(--blue); vertical-align: middle; margin-right: 13px;
  }

  .client-mark {
    position: absolute; left: 53px; top: 281px;
    display: flex; align-items: center; gap: 12px;
    font-size: 20px; font-weight: 600; letter-spacing: 0.2px;
  }
  .client-mark__dot {
    width: 44px; height: 44px; border-radius: 50%; background: var(--white);
  }

  .brand {
    position: absolute; left: 50px; top: 424px;
    font-weight: 600; line-height: 1; color: var(--white);
  }
  .brand__name { display: block; font-size: 40px; letter-spacing: 0.5px; }
  .brand__sub { display: block; font-size: 18px; letter-spacing: 1.5px; margin-top: 4px; padding-left: 2px; }

  .tagline {
    position: absolute; left: 431px; top: 441px;
    font-size: 21px; font-weight: 400; line-height: 1.4; text-transform: uppercase;
    letter-spacing: 0.2px;
  }
</style>
</head>
<body>

<section class="banner banner--employee">
  <div class="banner__photo" role="img" aria-label="Photo d'un centre d'appel : une employée souriante avec un casque-micro, collègue en arrière-plan"></div>
  <svg class="banner__shapes" viewBox="0 0 986 515" aria-hidden="true">
    <defs>
      <linearGradient id="steel-a" x1="0" y1="0" x2="1" y2="1">
        <stop offset="0" stop-color="var(--steel-1)"/>
        <stop offset="1" stop-color="var(--steel-2)"/>
      </linearGradient>
    </defs>
    <polygon points="0,0 415,0 0,72" fill="var(--blue-deep)"/>
    <polygon points="0,0 152,0 0,92" fill="var(--blue)"/>
    <polygon points="986,345 986,420 700,420" fill="var(--blue-deep)"/>
    <polygon points="986,370 986,420 870,420" fill="var(--blue)"/>
    <polygon points="0,398 274,398 386,515 0,515" fill="url(#steel-a)"/>
    <polyline points="0,398 274,398 386,515" fill="none" stroke="var(--blue)" stroke-width="3"/>
    <polygon points="308,418 986,418 986,515 400,515" fill="var(--panel)"/>
    <polyline points="986,418 308,418 400,515" fill="none" stroke="var(--blue)" stroke-width="3"/>
  </svg>
  <h2 class="headline">Ferlin Solutions <strong>est fier de compter</strong> parmi ses employés</h2>
  <div class="employee-portrait" role="img" aria-label="Zone photo de l'employé mis en avant"></div>
  <p class="employee-name">JULIEN RAVELLE</p>
  <div class="brand"><span class="brand__name">FERLIN</span><span class="brand__sub">SOLUTIONS</span></div>
  <p class="tagline">Centre d'appel spécialisé pour les<br>concessionnaires automobiles.</p>
</section>

<section class="banner banner--client">
  <div class="banner__photo" role="img" aria-label="Photo d'un coupé sport bleu-gris sur une route sinueuse avec un pont et des arbres"></div>
  <svg class="banner__shapes" viewBox="0 0 986 515" aria-hidden="true">
    <defs>
      <linearGradient id="steel-b" x1="0" y1="0" x2="1" y2="1">
        <stop offset="0" stop-color="var(--steel-1)"/>
        <stop offset="1" stop-color="var(--steel-2)"/>
      </linearGradient>
    </defs>
    <polygon points="0,0 415,0 0,72" fill="var(--blue-deep)"/>
    <polygon points="0,0 152,0 0,92" fill="var(--blue)"/>
    <polygon points="986,345 986,420 700,420" fill="var(--blue-deep)"/>
    <polygon points="986,370 986,420 870,420" fill="var(--blue)"/>
    <polygon points="0,398 274,398 386,515 0,515" fill="url(#steel-b)"/>
    <polyline points="0,398 274,398 386,515" fill="none" stroke="var(--blue)" stroke-width="3"/>
    <polygon points="308,418 986,418 986,515 400,515" fill="var(--panel)"/>
    <polyline points="986,418 308,418 400,515" fill="none" stroke="var(--blue)" stroke-width="3"/>
  </svg>
  <h2 class="headline">Ferlin Solutions est<br><strong>fier de compter</strong><br>parmi ses clients</h2>
  <div class="client-mark"><span class="client-mark__dot"></span><span>MARQUET MONTRÉAL</span></div>
  <div class="brand"><span class="brand__name">FERLIN</span><span class="brand__sub">SOLUTIONS</span></div>
  <p class="tagline">Centre d'appel spécialisé pour les<br>concessionnaires automobiles.</p>
</section>

</body>
</html>
```